Kestrelmoor Advisory Services LLC
The Quiet Hand Consutants
Project: Kestrelmoor Advisory Services LLC
Kestrelmoor Advisory Services LLC - Financial Services
Creative Brief
Professional
Warrick Dunstan Hollowell
Senior Managing Director
388 West 19th Street New York, N.T. 10024
whollowell@kmaservices.net
KESTRELMOORADVISORYSERVICES.COM

```html
<!DOCTYPE html>
<html lang="en">
<head>
<meta charset="utf-8">
<title>Kestrelmoor Advisory Services – Business Card</title>
<link href="https://fonts.googleapis.com/css2?family=Noto+Serif:ital,wght@0,400;0,700;1,400&display=swap" rel="stylesheet">
<style>
  :root {
    --page-bg: #e9e7e3;
    --card-white: #ffffff;
    --blue-deep: #0b3a86;
    --blue-mid: #1c5fb5;
    --blue-light: #3d8ad8;
    --gold: #c99a2e;
    --gold-light: #e3bf61;
    --text-light: #ffffff;
    --brand-blue: #1b4f9c;
  }
  * { margin: 0; padding: 0; box-sizing: border-box; }
  html, body { width: 1200px; height: 780px; overflow: hidden; }
  body {
    background: var(--page-bg);
    font-family: "Noto Serif", Georgia, serif;
    position: relative;
  }
  .business-card {
    position: absolute;
    left: 80px; top: 90px;
    width: 1040px; height: 600px;
    border-radius: 26px;
    overflow: hidden;
    background: var(--card-white);
    box-shadow: 0 10px 30px rgba(0,0,0,0.18);
  }
  .card-art { position: absolute; inset: 0; }
  .holder {
    position: absolute; left: 52px; top: 48px;
    color: var(--text-light);
  }
  .holder-name { font-size: 25px; font-weight: 700; letter-spacing: 0.2px; white-space: nowrap; }
  .holder-title { font-size: 22px; font-style: italic; margin-top: 4px; }
  .address {
    position: absolute; left: 52px; top: 250px;
    color: var(--text-light); font-size: 21px; line-height: 1.35; font-style: normal;
  }
  .contact-list {
    position: absolute; left: 52px; top: 352px;
    list-style: none; color: var(--text-light); font-size: 20px;
  }
  .contact-list li { display: flex; align-items: center; height: 38px; white-space: nowrap; }
  .contact-list svg { width: 22px; height: 22px; margin-right: 14px; fill: var(--text-light); flex: none; }
  .brand {
    position: absolute; left: 600px; top: 250px; width: 400px;
    text-align: center;
    color: var(--brand-blue);
    font-size: 34px; font-weight: 400; letter-spacing: 1px; line-height: 1.2;
  }
</style>
</head>
<body>
  <section class="business-card">
    <svg class="card-art" viewBox="0 0 1040 600" preserveAspectRatio="none">
      <defs>
        <linearGradient id="panelBlue" x1="0" y1="0" x2="1" y2="1">
          <stop offset="0" stop-color="#0b3a86"/>
          <stop offset="0.45" stop-color="#3d8ad8"/>
          <stop offset="1" stop-color="#1c5fb5"/>
        </linearGradient>
      </defs>
      <path class="gold-swoosh" d="M0,0 L500,0 C400,140 600,340 455,600 L0,600 Z" fill="#c99a2e"/>
      <path class="gold-edge" d="M0,0 L484,0 C386,140 584,340 440,600 L0,600 Z" fill="#e3bf61"/>
      <path class="blue-panel" d="M0,0 L472,0 C372,140 570,340 426,600 L0,600 Z" fill="url(#panelBlue)"/>
    </svg>

    <div class="holder">
      <div class="holder-name">Warrick Dunstan Hollowell</div>
      <div class="holder-title">Senior Managing Director</div>
    </div>

    <address class="address">
      388 West 19th Street<br>New York, N.T. 10024
    </address>

    <ul class="contact-list">
      <li><svg viewBox="0 0 24 24"><path d="M6.6 10.8a15 15 0 0 0 6.6 6.6l2.2-2.2c.3-.3.7-.4 1-.2 1.1.4 2.3.6 3.6.6.6 0 1 .4 1 1V20c0 .6-.4 1-1 1A17 17 0 0 1 3 4c0-.6.4-1 1-1h3.5c.6 0 1 .4 1 1 0 1.3.2 2.5.6 3.6.1.3 0 .7-.2 1z"/></svg>555-214-0381</li>
      <li><svg viewBox="0 0 24 24"><path d="M7 1h10a2 2 0 0 1 2 2v18a2 2 0 0 1-2 2H7a2 2 0 0 1-2-2V3a2 2 0 0 1 2-2zm0 3v14h10V4zm5 15.5a1.2 1.2 0 1 0 0 2.4 1.2 1.2 0 0 0 0-2.4z"/></svg>555-307-6142</li>
      <li><svg viewBox="0 0 24 24"><path d="M6 2h9l3 3v5H6zM3 11h18a1 1 0 0 1 1 1v8a1 1 0 0 1-1 1H3a1 1 0 0 1-1-1v-8a1 1 0 0 1 1-1zm3 3v2h4v-2zm0 3v2h4v-2z"/></svg>555-498-2275</li>
      <li><svg viewBox="0 0 24 24"><path d="M12 2a10 10 0 1 0 5 18.7l-1-1.7A8 8 0 1 1 20 12v1.2c0 1-.7 1.8-1.6 1.8S17 14.2 17 13.2V7h-2v1a5 5 0 1 0 .7 6.9A3.5 3.5 0 0 0 22 13.2V12A10 10 0 0 0 12 2zm0 13a3 3 0 1 1 0-6 3 3 0 0 1 0 6z"/></svg>whollowell@kmaservices.net</li>
      <li><svg viewBox="0 0 24 24"><path d="M12 2a10 10 0 1 0 0 20 10 10 0 0 0 0-20zm6.9 6h-3a15 15 0 0 0-1.4-3.9A8 8 0 0 1 18.9 8zM12 4c.8 1.2 1.5 2.5 1.9 4h-3.8c.4-1.5 1.1-2.8 1.9-4zM4.3 14a8 8 0 0 1 0-4h3.4a16 16 0 0 0 0 4zm.8 2h3a15 15 0 0 0 1.4 3.9A8 8 0 0 1 5.1 16zm3-8h-3a8 8 0 0 1 4.4-3.9C8.9 5.3 8.4 6.6 8.1 8zM12 20c-.8-1.2-1.5-2.5-1.9-4h3.8c-.4 1.5-1.1 2.8-1.9 4zm2.3-6H9.7a14 14 0 0 1 0-4h4.6a14 14 0 0 1 0 4zm.2 5.9c.6-1.2 1.1-2.5 1.4-3.9h3a8 8 0 0 1-4.4 3.9zm1.8-5.9a16 16 0 0 0 0-4h3.4a8 8 0 0 1 0 4z"/></svg>kestrelmooradvisoryservices.com</li>
    </ul>

    <div class="brand">KESTRELMOOR<br>ADVISORY SERVICES</div>
  </section>
</body>
</html>
```